Brindlecove (main name) sharpening systems(underneath)

Specializing in Knife, Scissors and Clipper sharpening, repair and maintenance.
I would like a logo designed that has at least one of the elements above showing what could happen as a result of the instrument being sharpened by my company as part of the logo (maybe the word Brindlecove being cut in half)

Target Market(s)

commercial (restaurants or any establishment that deals with food preparation, salons, barbershops) residential (any homes that use knives scissors or clippers)

Contact Information for Business Card

Name: Marcus Pellingham
Address: K240 Coral Vista Heights
Cell: 12465917362
Email: brindlecovehone@mailtrove.net

Requirements
Must have
• Brindlecove....sharpening systems clean front with strong logo indicating what we do as part of logo front of card
• Contact details: back of card
• we sharpen on site or pick up and drop off within 24hrs (at back of Card)
• telephone number: (at back) for contact
• address and other details (at back)

```html
<!DOCTYPE html>
<html lang="en">
<head>
<meta charset="utf-8">
<title>Brindlecove Business Card</title>
<link rel="stylesheet" href="https://fonts.googleapis.com/css2?family=Montserrat:wght@400;500;700&display=swap">
<style>
  :root {
    --backdrop: #2e2f31;
    --card-white: #ffffff;
    --brand-blue: #3bb3e0;
    --ink-grey: #58595b;
    --text-white: #ffffff;
  }
  * { box-sizing: border-box; margin: 0; padding: 0; }
  html, body {
    width: 1200px;
    height: 900px;
    overflow: hidden;
    background: var(--backdrop);
    font-family: "Montserrat", sans-serif;
  }
  .canvas { position: relative; width: 1200px; height: 900px; }

  .card {
    position: absolute;
    width: 560px;
    height: 320px;
    border-radius: 22px;
    background: var(--card-white);
    overflow: hidden;
  }
  .card--front { left: 110px; top: 90px; }
  .card--back { left: 530px; top: 490px; }

  /* Brand lockup */
  .brand-mark {
    position: absolute;
    left: 0; right: 0;
    display: flex;
    flex-direction: column;
    align-items: center;
  }
  .card--front .brand-mark { top: 52px; }
  .brand-mark__dot {
    width: 96px;
    height: 96px;
    border-radius: 50%;
    background: var(--brand-blue);
    margin-bottom: 14px;
  }
  .brand-mark__name {
    font-weight: 700;
    font-size: 34px;
    letter-spacing: 1px;
    color: var(--ink-grey);
    line-height: 1.1;
  }
  .brand-mark__tagline {
    font-weight: 500;
    font-size: 13px;
    letter-spacing: 3px;
    text-transform: uppercase;
    color: var(--brand-blue);
    margin-top: 4px;
  }
  .front-web {
    position: absolute;
    left: 0; right: 0;
    top: 266px;
    text-align: center;
    font-size: 17px;
    font-weight: 400;
    color: var(--ink-grey);
  }
  .front-web__domain { color: var(--brand-blue); }

  /* Back */
  .back-art { position: absolute; inset: 0; }
  .card--back .brand-mark {
    top: 66px;
    left: 10px;
    right: auto;
    width: 230px;
  }
  .card--back .brand-mark__dot { width: 84px; height: 84px; margin-bottom: 12px; }
  .card--back .brand-mark__name { font-size: 28px; }
  .card--back .brand-mark__tagline { font-size: 10px; letter-spacing: 2px; }

  .contact {
    position: absolute;
    right: 24px;
    top: 34px;
    text-align: right;
    color: var(--text-white);
  }
  .contact__name { font-size: 21px; font-weight: 700; letter-spacing: 0.3px; }
  .contact__role { font-size: 12px; font-weight: 400; margin-bottom: 14px; }
  .contact__line {
    font-size: 12px;
    line-height: 19px;
    display: flex;
    justify-content: flex-end;
    align-items: center;
    gap: 8px;
  }
  .contact__line svg { width: 11px; height: 11px; flex: none; }
  .contact__spacer { width: 11px; flex: none; }
  .contact__bold { font-weight: 700; }
  .service {
    margin-top: 14px;
    font-size: 11px;
    font-weight: 500;
    line-height: 16px;
    padding-right: 19px;
  }
</style>
</head>
<body>
<main class="canvas">

  <section class="card card--front" aria-label="Card front">
    <div class="brand-mark">
      <div class="brand-mark__dot"></div>
      <div class="brand-mark__name">Brindlecove</div>
      <div class="brand-mark__tagline">sharpening systems</div>
    </div>
    <p class="front-web">www.<span class="front-web__domain">brindlecove</span>.com</p>
  </section>

  <section class="card card--back" aria-label="Card back">
    <svg class="back-art" viewBox="0 0 560 320" width="560" height="320" aria-hidden="true">
      <path d="M150 0 H560 V320 H250 C290 200 270 60 150 0 Z" fill="var(--brand-blue)"/>
      <path d="M142 0 C262 60 282 200 242 320" fill="none" stroke="var(--ink-grey)" stroke-width="4"/>
    </svg>

    <div class="brand-mark">
      <div class="brand-mark__dot"></div>
      <div class="brand-mark__name">Brindlecove</div>
      <div class="brand-mark__tagline">sharpening systems</div>
    </div>

    <div class="contact">
      <div class="contact__name">Marcus Pellingham</div>
      <div class="contact__role">Director</div>
      <div class="contact__line"><span>K240 Coral Vista Heights</span><span class="contact__spacer"></span></div>
      <div class="contact__line">
        <span>12465917362</span>
        <svg viewBox="0 0 12 12"><path d="M3 1 L5 3.5 L4 5 Q5 7 7 8 L8.5 7 L11 9 L9.5 11 Q5 11 1 5 Z" fill="var(--text-white)"/></svg>
      </div>
      <div class="contact__line">
        <span>brindlecovehone@mailtrove.net</span>
        <svg viewBox="0 0 12 12"><rect x="1" y="2.5" width="10" height="7" fill="none" stroke="var(--text-white)" stroke-width="1.2"/><path d="M1 2.5 L6 6.5 L11 2.5" fill="none" stroke="var(--text-white)" stroke-width="1.2"/></svg>
      </div>
      <div class="contact__line">
        <span>www.<span class="contact__bold">brindlecove</span>.com</span>
        <svg viewBox="0 0 12 12"><circle cx="6" cy="6" r="5" fill="none" stroke="var(--text-white)" stroke-width="1.1"/><ellipse cx="6" cy="6" rx="2.2" ry="5" fill="none" stroke="var(--text-white)" stroke-width="1"/><path d="M1 6 H11" stroke="var(--text-white)" stroke-width="1"/></svg>
      </div>
      <p class="service">On-site sharpening or<br>24hr pick-up &amp; drop-off</p>
    </div>
  </section>

</main>
</body>
</html>
```